Direct Mail flyer for the timeshare industry.

We need someone who has experience in direct mail experience in postcards and successful campaigns. The post card we are using is not good at all.

We are looking at a 5.5 x 8.5 postcard with 4 color on one side and the black and white on the mailing side. But if someone has a better idea instead of a postcard then I am open to that

Target Market(s)

Timeshare owners...most of them are 55 plus in age. We help people get out of their time share

Industry/Entity Type

Industry

Font styles to use
Serif

Colors

Designer to choose colors to be used in the design.

Requirements
Must have
• Call to action and be easy to understand and look very professional and not fake or cheesy

```html
<!DOCTYPE html>
<html lang="en">
<head>
<meta charset="utf-8">
<title>Private Event Invitation Postcard</title>
<link rel="stylesheet" href="https://fonts.googleapis.com/css2?family=Open+Sans:wght@400;600;700&family=Oswald:wght@400;500&display=swap">
<style>
  :root {
    --page: #f4f4f4;
    --card: #ececec;
    --card-back: #ededed;
    --ink: #1f1f1f;
    --muted: #555;
    --blue: #2aa4e0;
    --blue-band: rgba(52, 170, 226, 0.82);
    --red: #b72b2b;
    --red-deep: #8e1d1d;
    --red-band: rgba(190, 52, 36, 0.9);
    --line: #9a9a9a;
    --stamp: #d3d3d3;
  }
  * { box-sizing: border-box; margin: 0; padding: 0; }
  html, body { width: 889px; height: 1200px; overflow: hidden; }
  body {
    background: var(--page);
    font-family: "Open Sans", Arial, sans-serif;
    color: var(--ink);
    position: relative;
  }
  .postcard {
    position: absolute;
    left: 64px;
    width: 760px;
    height: 492px;
    overflow: hidden;
    box-shadow: 0 3px 10px rgba(0,0,0,0.22);
  }
  .postcard--front { top: 50px; background: var(--card); }
  .postcard--back { top: 640px; background: var(--card-back); }

  /* Front: photo side */
  .front-art { position: absolute; inset: 0; }
  .invite-heading {
    position: absolute;
    left: 20px; width: 400px; top: 34px;
    text-align: center;
  }
  .invite-title {
    font-size: 25px; font-weight: 600; color: var(--blue);
    letter-spacing: 0.3px;
  }
  .invite-subtitle {
    font-size: 19px; font-weight: 700; margin-top: 2px; letter-spacing: 0.3px;
  }
  .invite-lede {
    font-size: 13px; line-height: 20px; margin-top: 10px;
  }
  .invite-lede .free { color: var(--red); }

  .feature {
    position: absolute;
    width: 170px; height: 142px;
    border: 1.5px dotted #444;
    text-align: center;
    padding: 14px 6px 0;
  }
  .feature h2 {
    font-size: 14px; font-weight: 600; color: var(--red);
    margin-bottom: 10px; letter-spacing: 0.2px;
  }
  .feature p { font-size: 9.5px; line-height: 16px; color: var(--muted); }
  .feature--education { left: 22px; top: 180px; }
  .feature--protection { left: 208px; top: 180px; }
  .feature--advisement { left: 22px; top: 336px; }
  .feature--contact { left: 208px; top: 336px; }
  .feature--contact p { color: var(--ink); font-size: 10.5px; line-height: 17px; }
  .feature--contact .event-date {
    margin-top: 5px; font-size: 9.5px; line-height: 15px; color: var(--muted);
    white-space: nowrap;
  }

  .cta-band {
    position: absolute;
    font-family: "Oswald", "Arial Narrow", sans-serif;
    color: #fff;
    letter-spacing: 0.5px;
  }
  .cta-band--call {
    left: 432px; top: 150px; width: 310px; height: 44px;
    background: var(--blue-band);
    font-size: 21px; line-height: 44px; padding-left: 12px;
  }
  .cta-band--rsvp {
    left: 496px; top: 212px; width: 264px; height: 62px;
    background: var(--red-band);
    padding: 6px 0 0 14px;
  }
  .cta-band--rsvp .code { font-size: 21px; line-height: 26px; display: block; }
  .cta-band--rsvp .guarantee { font-size: 13px; line-height: 20px; display: block; letter-spacing: 0.8px; }

  /* Back: mailing side */
  .stamp-box {
    position: absolute; left: 602px; top: 26px;
    width: 96px; height: 96px;
    background: var(--stamp); border: 1.5px solid #8a8a8a;
  }
  .address-lines { position: absolute; left: 408px; top: 148px; width: 292px; }
  .address-lines span { display: block; height: 34px; border-bottom: 1.5px solid var(--line); }
  .contact-tab {
    position: absolute; left: 0; top: 136px;
    width: 220px; height: 26px;
    background: var(--ink);
    clip-path: polygon(0 0, 100% 0, 90% 100%, 0 100%);
    color: #fff; font-weight: 700; font-size: 14px;
    letter-spacing: 1px; line-height: 26px; padding-left: 72px;
  }
  .sender {
    position: absolute; left: 50px; top: 182px;
    font-size: 10px; line-height: 15px; color: #666;
  }
  .sender-phone-icon { position: absolute; left: 66px; top: 244px; }
  .sender-phone { position: absolute; left: 50px; top: 276px; font-size: 10px; color: #666; }
</style>
</head>
<body>

<section class="postcard postcard--front" aria-label="Invitation side">
  <svg class="front-art" width="760" height="492" viewBox="0 0 760 492">
    <defs>
      <linearGradient id="resort-fill" x1="0" y1="0" x2="0" y2="1">
        <stop offset="0" stop-color="#6fa9dd"/>
        <stop offset="0.45" stop-color="#7fae6a"/>
        <stop offset="0.7" stop-color="#3fa9d6"/>
        <stop offset="1" stop-color="#d9d2c3"/>
      </linearGradient>
    </defs>
    <polygon points="520,0 760,0 760,492 452,492 470,260" fill="url(#resort-fill)" role="img" aria-label="Photo of a resort pool with palm trees and villas"/>
    <polygon points="470,0 560,0 500,120 474,176" fill="var(--red-deep)"/>
    <polygon points="448,0 470,0 474,176 470,260 452,492 436,492" fill="var(--blue)"/>
    <polygon points="430,0 440,0 430,492 420,492" fill="var(--blue)"/>
    <polygon points="462,260 470,260 452,492 444,492" fill="var(--red)"/>
    <polygon points="560,0 572,0 510,120 500,120" fill="#ffffff"/>
  </svg>

  <header class="invite-heading">
    <h1 class="invite-title">A PRIVATE EVENT INVITATION</h1>
    <p class="invite-subtitle">LIMITED SEATING</p>
    <p class="invite-lede">This is your chance!<br>We’ve arranged for you and one guest to<br>attend our Harbor Point Group Event <span class="free">FREE of charge.</span></p>
  </header>

  <div class="feature feature--education">
    <h2>EDUCATION</h2>
    <p>We promise this event will be an eye-opening experience and an incredible learning opportunity regardless of your current situation.</p>
  </div>
  <div class="feature feature--protection">
    <h2>PROTECTION</h2>
    <p>Arm yourself with the knowledge of how to avoid the current scams occurring in the timeshare industry to protect you as an owner.</p>
  </div>
  <div class="feature feature--advisement">
    <h2>ADVISEMENT</h2>
    <p>Your questions are welcomed and will be addressed. This will bring you the sense of confidence that you have been seeking.</p>
  </div>
  <div class="feature feature--contact">
    <h2>CONTACT US</h2>
    <p>Lakeside Conference Inn<br>1200 Parkway Drive<br>Cedar Falls, TX 75000</p>
    <p class="event-date">Saturday, February 17, 2018<br>10:30 AM | 3:00 PM | 6:00 PM</p>
  </div>

  <div class="cta-band cta-band--call">CALL (888) 555-0147 TODAY WITH</div>
  <div class="cta-band cta-band--rsvp">
    <span class="code">RSVP CODE # HPG70218</span>
    <span class="guarantee">TO GUARANTEE YOUR SEATS!</span>
  </div>
</section>

<section class="postcard postcard--back" aria-label="Mailing side">
  <div class="contact-tab">GET IN TOUCH</div>
  <p class="sender">Harbor Point Group, LLC<br>2210 W Maple Ridge Road<br>Fairview, Mo. 65000</p>
  <svg class="sender-phone-icon" width="16" height="16" viewBox="0 0 24 24" aria-hidden="true">
    <circle cx="12" cy="12" r="12" fill="#333"/>
    <path d="M8 6.5c.6-.5 1.3-.4 1.7.2l1 1.6c.3.5.2 1.1-.2 1.4l-.7.6c.6 1.4 1.6 2.4 3 3l.6-.7c.4-.4 1-.5 1.4-.2l1.6 1c.6.4.7 1.1.2 1.7l-.8.9c-.6.6-1.6.8-2.4.4-2.8-1.3-4.9-3.4-6.2-6.2-.4-.8-.2-1.8.4-2.4z" fill="#fff"/>
  </svg>
  <p class="sender-phone">(888) 555-0147</p>
  <div class="stamp-box"></div>
  <div class="address-lines"><span></span><span></span><span></span><span></span><span></span></div>
</section>

</body>
</html>
```